Construction Company

I'm a new construction company called Tembrik Construction. I want my card to look simple and clean. I have provided a sample of what I want the front to look like (Tembrik_Card.jpeg) and a back ground for the back of the (Tembrik_Card_Background.jpeg) - the background can be faded so my name and other information is more prominent.
Construction

```html
<!DOCTYPE html>
<html lang="en">
<head>
<meta charset="utf-8">
<title>Tembrik Construction – Business Card</title>
<link rel="stylesheet" href="https://fonts.googleapis.com/css2?family=Open+Sans:ital,wght@0,400;1,700&display=swap">
<style>
  :root {
    --page: #f4f4f4;
    --card: #ffffff;
    --band: #4a442e;
    --ink: #3f3a26;
    --rule: #3a3524;
    --brand-ink: #f2efe6;
    --plan-light: #fafafa;
    --plan-mid: #ececec;
  }
  * { margin: 0; padding: 0; box-sizing: border-box; }
  html, body { width: 934px; height: 1200px; overflow: hidden; background: var(--page); }
  .card {
    position: absolute; left: 33px; top: 59px; width: 869px; height: 1079px;
    background: var(--card);
    box-shadow: 0 0 18px rgba(0,0,0,0.08);
    font-family: "Open Sans", sans-serif;
    color: var(--ink);
  }
  .card__plan {
    position: absolute; left: 2px; top: 0; width: 650px; height: 480px;
    background: radial-gradient(ellipse at 50% 50%, var(--plan-mid) 0%, var(--plan-light) 65%, var(--card) 100%);
  }
  .identity__name {
    position: absolute; left: 459px; top: 176px;
    font-size: 32px; font-weight: 700; font-style: italic; line-height: 1;
  }
  .identity__rule {
    position: absolute; left: 421px; top: 222px; width: 413px; height: 2px;
    background: var(--rule);
  }
  .identity__title {
    position: absolute; left: 461px; top: 236px;
    font-size: 30px; font-weight: 400; line-height: 1;
  }
  .contact { position: absolute; left: 446px; top: 314px; list-style: none; }
  .contact__item {
    display: flex; align-items: center; height: 42px;
    font-size: 21px; line-height: 1;
  }
  .contact__icon { width: 30px; height: 30px; margin-right: 19px; flex: none; }
  .band {
    position: absolute; left: 0; top: 540px; width: 869px; height: 539px;
    background: var(--band);
    display: flex; align-items: center; justify-content: center;
  }
  .brand {
    font-family: "Open Sans", sans-serif; font-weight: 400; font-style: normal;
    font-size: 52px; line-height: 1; color: var(--brand-ink);
    white-space: nowrap;
  }
</style>
</head>
<body>
  <div class="card">
    <div class="card__plan" role="img" aria-label="Faded architectural floor plan of a house"></div>

    <div class="identity__name">Name</div>
    <div class="identity__rule"></div>
    <div class="identity__title">Title</div>

    <ul class="contact">
      <li class="contact__item">
        <svg class="contact__icon" viewBox="0 0 30 30"><path d="M12 5c2 0 3 2 3 3s-2 2-2 3 0 6 1 7 2 0 3 1 0 4-2 5c-3 1-4-2-4-5s-1-7 0-11 1-3 1-3z" fill="var(--ink)"/></svg>
        <span>+(000) 1234 5678</span>
      </li>
      <li class="contact__item">
        <svg class="contact__icon" viewBox="0 0 30 30" fill="none" stroke="var(--ink)" stroke-width="1.6"><rect x="9" y="4" width="12" height="12"/><line x1="11" y1="8" x2="19" y2="8"/><line x1="11" y1="11" x2="19" y2="11"/><rect x="4" y="16" width="22" height="10"/><line x1="8" y1="21" x2="22" y2="21"/></svg>
        <span>name@emailaddress.com</span>
      </li>
      <li class="contact__item">
        <svg class="contact__icon" viewBox="0 0 30 30"><path d="M15 3a8 8 0 0 0-8 8c0 6 8 16 8 16s8-10 8-16a8 8 0 0 0-8-8zm0 11a3.5 3.5 0 1 1 0-7 3.5 3.5 0 0 1 0 7z" fill="var(--ink)"/></svg>
        <span>your address, address 1</span>
      </li>
      <li class="contact__item">
        <svg class="contact__icon" viewBox="0 0 30 30" fill="none" stroke="var(--ink)" stroke-width="1.3"><circle cx="15" cy="15" r="12"/><ellipse cx="15" cy="15" rx="5" ry="12"/><line x1="3" y1="15" x2="27" y2="15"/><path d="M5 9h20M5 21h20"/></svg>
        <span>www.website.com</span>
      </li>
    </ul>

    <div class="band">
      <span class="brand">Tembrik Construction</span>
    </div>
  </div>
</body>
</html>
```